Specialized tax accounting firm needs marketing postcard

We need a postcard design for a professional services firm called R. Winslow Farrow Inc. The firm is essentially a very specialized tax accounting firm - instead of serving the end consumer, we support other public accounting firms in the area of Canadian and U.S. tax advisory and compliance (i.e. they call us on tax issues too complex for the general practitioner). Our byline is "Tax Support Services for Public Accounting Firms". Our postcard should utilize our logo and be based on colours present in our logo (see file attached). The final design needs to convey professionalism and trustworthiness (we're hired by accountants after all!) while being creative and eye-catching. Eye-catching is critical, since many prospective recipients will not have heard from me before and I want them to read the postcard.

I've attached:
The font used in the logo
The logo itself in a variety of file formats
A picture of myself for incorporation in the postcard
A sample postcard from Publisher showing the wording to be used in the postcard and the elements to be included

Please note that in including a draft postcard I don't want the designer to follow the layout as is. It just shows the basic elements I want included. The only element which should remain constant is the wording - I do want the text elements included as written - however, everything else - font, size, placement of elements, etc. is up for creative ideas.

Please note that there is much more leather background around the logo than needs to be incorporated in the letterhead.

Industry/Entity Type

Accounting

```html
<!DOCTYPE html>
<html lang="en">
<head>
<meta charset="utf-8">
<title>R. Winslow Farrow Inc. – Postcard</title>
<link href="https://fonts.googleapis.com/css2?family=Cinzel:wght@400;600&display=swap" rel="stylesheet">
<style>
  :root{
    --stage:#939598;
    --paper:#ffffff;
    --orange:#f5961e;
    --gold:#efbd50;
    --navy:#1f2a6b;
    --sky:#1e90d6;
    --ink-dark:#141414;
    --leather:#2a2a2a;
    --white:#ffffff;
  }
  *{margin:0;padding:0;box-sizing:border-box}
  html,body{width:1200px;height:882px;overflow:hidden;background:var(--paper)}
  .stage{position:absolute;left:0;top:0;width:1142px;height:882px;background:var(--stage)}
  .card{position:absolute;top:258px;width:488px;height:373px;box-shadow:8px 10px 12px rgba(0,0,0,.45);font-family:"Cinzel",serif;overflow:hidden}

  .brand{position:absolute;display:flex;align-items:flex-start}
  .brand__mark{flex:none;background:var(--navy)}
  .brand__text{flex:none}
  .brand__name{color:var(--white);font-weight:400;white-space:nowrap;letter-spacing:.02em;line-height:1}
  .brand__inc{display:flex;align-items:center;color:var(--white);line-height:1}
  .brand__inc::before,.brand__inc::after{content:"";flex:1;height:1px;background:var(--white)}
  .brand__tag{white-space:nowrap;line-height:1}

  /* back side */
  .card--back{left:49px;background:linear-gradient(90deg,var(--orange) 0%,var(--gold) 38%,var(--gold) 70%,var(--orange) 100%)}
  .card--back .brand{left:21px;top:42px}
  .card--back .brand__mark{width:38px;height:38px;margin-right:8px}
  .card--back .brand__text{width:226px}
  .card--back .brand__name{font-size:20px}
  .card--back .brand__inc{font-size:8px;gap:4px;margin-top:2px}
  .card--back .brand__tag{font-size:7px;letter-spacing:.05em;color:var(--navy);margin-top:4px;font-weight:600}

  .intro{position:absolute;left:21px;top:135px;width:330px;font-size:9.4px;line-height:11.6px;color:var(--navy);font-weight:600}
  .accent-bar{position:absolute;left:22px;top:200px;width:405px;height:18px;background:var(--sky)}
  .contact{position:absolute;left:21px;top:240px;font-size:9px;line-height:11.7px;color:var(--white)}
  .contact__lead{margin-bottom:1px}
  .address-lines{position:absolute;left:189px;top:264px;width:276px}
  .address-lines span{display:block;height:1px;background:var(--navy);margin-bottom:11.6px}

  /* front side */
  .card--front{left:608px;background:radial-gradient(ellipse at 45% 25%,var(--leather) 0%,#1c1c1c 45%,var(--ink-dark) 100%)}
  .portrait{position:absolute;left:322px;top:64px;width:150px;height:200px;background:radial-gradient(ellipse at 50% 30%,#6b5b52 0%,#2e2e33 55%,rgba(20,20,20,0) 80%)}
  .card--front .brand{left:14px;top:220px}
  .card--front .brand__mark{width:63px;height:63px;margin-right:13px;background:var(--orange)}
  .card--front .brand__text{width:382px}
  .card--front .brand__name{font-size:33px}
  .card--front .brand__inc{font-size:13px;gap:6px;margin-top:3px}
  .card--front .brand__tag{font-size:11.5px;letter-spacing:.09em;color:var(--white);margin-top:5px}
  .front-bar{position:absolute;left:15px;top:296px;width:457px;height:10px;background:var(--white)}
</style>
</head>
<body>
<div class="stage">

  <section class="card card--back">
    <div class="brand">
      <div class="brand__mark"></div>
      <div class="brand__text">
        <div class="brand__name">R. WINSLOW FARROW</div>
        <div class="brand__inc">INC</div>
        <div class="brand__tag">Tax support services for public accounting firms</div>
      </div>
    </div>

    <p class="intro">R. Winslow Farrow Inc. is a boutique tax accounting firm specializing in tax support for public accounting firms. However, I also provide Canadian and U.S. tax advisory and compliance services to the general public.</p>

    <div class="accent-bar"></div>

    <div class="contact">
      <p class="contact__lead">Please feel free to contact me if I can be of assistance to you or to your clients.</p>
      <p>Ronald W. Farrow, CGA<br>
      R. Winslow Farrow Inc.<br>
      18-410 Kestrel Road<br>
      Halifax, NS B3K 2P4<br>
      (902) 555-0148<br>
      ronald@farrowtax.services<br>
      www.farrowtax.services</p>
    </div>

    <div class="address-lines"><span></span><span></span><span></span><span></span><span></span><span></span></div>
  </section>

  <section class="card card--front">
    <div class="portrait" role="img" aria-label="Portrait photo of the firm's principal in a dark suit, arms crossed"></div>
    <div class="brand">
      <div class="brand__mark"></div>
      <div class="brand__text">
        <div class="brand__name">R. WINSLOW FARROW</div>
        <div class="brand__inc">INC</div>
        <div class="brand__tag">Tax support services for public accounting firms</div>
      </div>
    </div>
    <div class="front-bar"></div>
  </section>

</div>
</body>
</html>
```